Meridale Wall Tracking Office

I have a current web site that it looking quite aged and it needs a new lease of life. This is a Graffiti Management Website so is all about data processing and management of information. I want a html 5 view on any platform design. clean crisp and new. I have provided some screen shots of my current site.

Target Market(s)

The Target Market will be local government. most users will not be heavy pc users

Industry/Entity Type

Management

Font styles to use
Sans Serif
Other font styles liked:
• web font like calibri

Colors

Designer to choose colors to be used in the design.

Requirements
Must have
• Must have menus similar to attachments

```html
<!DOCTYPE html>
<html lang="en">
<head>
<meta charset="utf-8">
<title>Meridale Wall Tracking Office</title>
<link href="https://fonts.googleapis.com/css2?family=Open+Sans:wght@300;400;600;700&display=swap" rel="stylesheet">
<style>
:root{
  --blue:#1b75bb;
  --teal:#2aa3d8;
  --navy:#174766;
  --navy-dark:#1d2e3d;
  --ink:#222;
  --text:#444;
  --muted:#9a9a9a;
  --line:#d9d9d9;
  --panel:#1c1c1c;
  --footer:#232323;
  --white:#fff;
  --soft:#f2f2f2;
}
*{box-sizing:border-box;margin:0;padding:0}
html,body{width:1200px;height:2975px;overflow:hidden}
body{position:relative;background:var(--white);font-family:"Open Sans",Arial,sans-serif;color:var(--text)}
.abs{position:absolute}

/* header */
.site-header{position:absolute;left:0;top:0;width:1200px;height:130px;background:var(--white)}
.brand{position:absolute;left:32px;top:18px;color:var(--blue);font-weight:700;line-height:1}
.brand-short{font-size:58px;letter-spacing:2px}
.brand-long{font-size:17px;letter-spacing:1px;margin-top:4px}
.main-nav{position:absolute;right:20px;top:45px;display:flex;gap:6px}
.main-nav a{display:block;height:44px;line-height:44px;padding:0 12px;font-size:17px;font-weight:700;color:var(--ink);text-decoration:none}
.main-nav a.active{background:var(--blue);color:var(--white)}

/* hero */
.hero-image{position:absolute;left:0;top:130px;width:1200px;height:670px;
  background:linear-gradient(120deg,#7a3b2f 0%,#c4504a 25%,#e28b9a 45%,#3d5fa6 62%,#b8743c 80%,#6b4a38 100%)}
.hero-panel{position:absolute;left:0;top:355px;width:645px;height:385px;background:var(--panel);opacity:.96;padding:50px 0 0 64px;color:var(--white);box-shadow:0 8px 20px rgba(0,0,0,.4)}
.hero-title{font-size:42px;font-weight:300;line-height:1.2;letter-spacing:.5px}
.hero-lead{font-size:17px;margin-top:24px;line-height:1.45;width:520px}
.btn{position:absolute;display:block;width:212px;height:60px;line-height:60px;text-align:center;font-size:22px;font-weight:700;text-decoration:none}
.btn-login{left:124px;top:260px;background:var(--blue);color:var(--white)}
.btn-register{left:360px;top:260px;background:var(--white);color:var(--ink)}

/* headings */
.section-title{position:absolute;font-size:33px;font-weight:400;color:var(--teal);letter-spacing:1px;text-align:center}
.section-title::after{content:"";display:block;width:40px;height:2px;background:var(--line);margin:10px auto 0}
.section-title.left::after{margin-left:70px}

/* about */
.about-text{position:absolute;left:250px;top:925px;width:700px;text-align:center;font-size:17px;line-height:1.4;color:var(--text)}
.about-text b{color:var(--teal);font-weight:400}
.team{position:absolute;left:112px;top:1078px;width:900px;display:flex;gap:33px}
.member{width:124px;text-align:center}
.avatar{width:124px;height:124px;border-radius:50%;background:radial-gradient(circle at 50% 40%,#e8c8b0,#9a7a66);border:3px solid #eee}
.member-name{font-size:10px;color:#aaa;letter-spacing:1.5px;margin-top:14px;line-height:1.4}
.member-rule{width:40px;height:2px;background:var(--line);margin:28px auto 0}

/* products */
.product-grid{position:absolute;left:94px;top:1413px;width:1012px;display:grid;grid-template-columns:repeat(3,325px);grid-auto-rows:228px;gap:18px 18px}
.product{background:var(--navy);color:var(--white);text-align:center;font-size:14px;padding-top:62px}
.product.dark{background:var(--navy-dark)}
.product-icon{width:54px;height:54px;border:1.5px solid rgba(255,255,255,.7);border-radius:50%;margin:0 auto 26px;display:flex;align-items:center;justify-content:center}

/* benefits */
.divider{position:absolute;left:595px;top:1958px;width:1px;height:720px;background:var(--line)}
.benefit{position:absolute;left:104px;width:460px}
.benefit-icon{position:absolute;left:0;top:0;width:74px;height:74px;border-radius:50%;border:2px solid #cfe6f5;display:flex;align-items:center;justify-content:center}
.benefit-body{position:absolute;left:94px;top:0;width:360px}
.benefit-title{font-size:15px;font-weight:700;color:var(--ink);padding-bottom:8px;border-bottom:1px solid var(--line);width:180px}
.benefit-text{font-size:13px;line-height:1.5;margin-top:18px}
.btn-more{position:absolute;left:243px;top:2640px;width:139px;height:40px;line-height:40px;background:var(--teal);color:var(--white);text-align:center;font-size:16px;text-decoration:none}

/* report */
.report-text{position:absolute;left:625px;width:510px;font-size:13px;line-height:1.45;color:var(--ink)}
.stats{position:absolute;left:625px;top:2127px;width:466px;height:203px;background:var(--soft);padding:14px 0 0 0}
.stat{position:relative;height:60px;margin:0 10px}
.stat-label{position:absolute;left:0;top:10px;font-size:12px;color:var(--ink)}
.stat-bar{position:absolute;left:0;top:32px;width:280px;height:5px;background:#ccc}
.stat-bar i{display:block;height:5px;background:var(--teal)}
.stat-value{position:absolute;left:290px;top:0;font-size:36px;color:var(--ink);font-weight:400;letter-spacing:-1px}
.stat-change{position:absolute;left:392px;top:8px;font-size:10px;color:#888;line-height:1.4}
.stat-change em{font-style:normal;color:#d33}
.pie{position:absolute;left:744px;top:2372px}

/* footer */
.site-footer{position:absolute;left:0;top:2759px;width:1200px;height:216px;background:var(--footer);color:var(--white)}
.footer-brand{position:absolute;left:80px;top:36px;font-weight:700;line-height:1}
.footer-brand .brand-short{font-size:62px;letter-spacing:3px}
.footer-brand .brand-long{font-size:19px}
.copyright{position:absolute;left:88px;top:140px;font-size:11px}
.footer-contact{position:absolute;left:450px;top:50px;width:270px;text-align:center;font-size:14px;line-height:1.5}
.footer-contact h3{font-size:16px;font-weight:700;margin-bottom:22px}
.footer-contact p{margin-bottom:16px}
.footer-address{position:absolute;left:800px;top:68px;width:290px;text-align:center;font-size:14px;line-height:1.4}
.socials{position:absolute;left:852px;top:132px;display:flex;gap:12px}
.socials span{width:30px;height:30px;border-radius:50%;background:var(--teal);display:block}
</style>
</head>
<body>

<header class="site-header">
  <div class="brand">
    <div class="brand-short">MWTO</div>
    <div class="brand-long">MERIDALE WALL TRACKING OFFICE</div>
  </div>
  <nav class="main-nav">
    <a class="active" href="#">HOME</a>
    <a href="#">PRODUCTS</a>
    <a href="#">REPORTS</a>
    <a href="#">BENEFITS</a>
    <a href="#">LEGISLATION</a>
    <a href="#">CONTACT US</a>
  </nav>
</header>

<section>
  <div class="hero-image" role="img" aria-label="Colourful graffiti mural of a masked superhero on a brick wall"></div>
  <div class="hero-panel">
    <h1 class="hero-title">HELPING YOU CLEAN UP<br>YOUR COMMUNITY</h1>
    <p class="hero-lead">MWTO is an Online Database System to Manage Graffiti in your area or Your Properties</p>
    <a class="btn btn-login" href="#">LOGIN</a>
    <a class="btn btn-register" href="#">REGISTER</a>
  </div>
</section>

<section>
  <h2 class="section-title" style="left:450px;top:835px;width:300px">ABOUT US</h2>
  <p class="about-text"><b>MWTO</b> is an Online Database System to Manage Graffiti in your area or Your Properties. <b>MWTO</b> allows sharing of Critical Graffiti Tag and Photographic Data between its subscribers, assisting with tracking down Serial Graffiti Offenders. <b>MWTO</b> allows you to Register, Track, Report and Archive Graffiti Jobs with Photographic Records.</p>
  <div class="team">
    <div class="member"><div class="avatar" role="img" aria-label="Team member portrait"></div><div class="member-name">LENA MARSH<br>(MANAGER)</div><div class="member-rule"></div></div>
    <div class="member"><div class="avatar" role="img" aria-label="Team member portrait"></div><div class="member-name">TOM GARRETT<br>(SUPPORT)</div><div class="member-rule"></div></div>
    <div class="member"><div class="avatar" role="img" aria-label="Team member portrait"></div><div class="member-name">KATE DOBSON<br>(LIAISON)</div><div class="member-rule"></div></div>
    <div class="member"><div class="avatar" role="img" aria-label="Team member portrait"></div><div class="member-name">RYAN HOLT<br>(FINANCE)</div><div class="member-rule"></div></div>
    <div class="member"><div class="avatar" role="img" aria-label="Team member portrait"></div><div class="member-name">APRIL VANCE<br>(DEVELOPER)</div><div class="member-rule"></div></div>
    <div class="member"><div class="avatar" role="img" aria-label="Team member portrait"></div><div class="member-name">JAMES PRIOR<br>(MANAGER)</div><div class="member-rule"></div></div>
  </div>
</section>

<section>
  <h2 class="section-title" style="left:450px;top:1335px;width:300px">PRODUCTS</h2>
  <div class="product-grid">
    <div class="product"><div class="product-icon"><svg width="20" height="26" viewBox="0 0 20 26"><rect x="5" y="6" width="10" height="18" rx="2" fill="none" stroke="#fff" stroke-width="1.5"/><rect x="7" y="1" width="6" height="5" fill="#fff"/></svg></div>GRAFFITI REGISTER</div>
    <div class="product"><div class="product-icon"><svg width="26" height="22" viewBox="0 0 26 22"><rect x="1" y="1" width="24" height="20" fill="none" stroke="#fff" stroke-width="1.5"/><path d="M4 18l6-7 5 5 3-3 4 5z" fill="#fff"/></svg></div>GRAFFITI PHOTOS</div>
    <div class="product"><div class="product-icon"><svg width="22" height="26" viewBox="0 0 22 26"><path d="M2 1h13l5 5v19H2z" fill="none" stroke="#fff" stroke-width="1.5"/><path d="M11 9v9M7 14l4 4 4-4" fill="none" stroke="#fff" stroke-width="1.5"/></svg></div>GRAFFITI ARCHIVE</div>
    <div class="product"><div class="product-icon"><svg width="26" height="24" viewBox="0 0 26 24"><rect x="1" y="1" width="20" height="16" fill="none" stroke="#fff" stroke-width="1.5"/><circle cx="15" cy="14" r="4" fill="none" stroke="#fff" stroke-width="1.5"/><path d="M18 17l5 5" stroke="#fff" stroke-width="2"/></svg></div>SEARCHABLE DATABASE</div>
    <div class="product dark"><div class="product-icon"><svg width="24" height="22" viewBox="0 0 24 22"><path d="M1 1v20h22" fill="none" stroke="#fff" stroke-width="1.5"/><path d="M4 16l6-7 4 4 7-9" fill="none" stroke="#fff" stroke-width="1.5"/></svg></div>STATISITCAL ANALYSIS REPORTS</div>
    <div class="product"><div class="product-icon"><svg width="26" height="20" viewBox="0 0 26 20"><rect x="1" y="3" width="12" height="10" rx="2" fill="none" stroke="#fff" stroke-width="1.5"/><rect x="12" y="8" width="12" height="10" rx="2" fill="none" stroke="#fff" stroke-width="1.5"/></svg></div>DATA CONVERSION</div>
  </div>
</section>

<section>
  <h2 class="section-title left" style="left:119px;top:1960px;text-align:left">BENEFITS</h2>
  <div class="divider"></div>

  <div class="benefit" style="top:2060px">
    <div class="benefit-icon"><svg width="34" height="30" viewBox="0 0 34 30"><path d="M3 20l8-8 6 3 12-12" fill="none" stroke="#2aa3d8" stroke-width="2.5"/><rect x="3" y="22" width="28" height="5" fill="#2aa3d8"/></svg></div>
    <div class="benefit-body"><div class="benefit-title">GRAFFITI REGISTER</div><p class="benefit-text">MWTO allows you to track the cost and effectiveness of your Graffiti Removal. Compare .....</p></div>
  </div>
  <div class="benefit" style="top:2215px">
    <div class="benefit-icon"><svg width="30" height="26" viewBox="0 0 30 26"><rect x="2" y="2" width="26" height="22" fill="none" stroke="#2aa3d8" stroke-width="2"/><path d="M6 20l7-8 5 5 3-3 5 6z" fill="#2aa3d8"/></svg></div>
    <div class="benefit-body"><div class="benefit-title">PHOTOGRAPHIC RECORDS</div><p class="benefit-text">Store any photographic records of New, Existing and Completed Graffiti Jobs. Archive all...</p></div>
  </div>
  <div class="benefit" style="top:2355px">
    <div class="benefit-icon"><svg width="34" height="32" viewBox="0 0 34 32"><circle cx="10" cy="6" r="4" fill="#2aa3d8"/><circle cx="24" cy="6" r="4" fill="#2aa3d8"/><rect x="6" y="12" width="8" height="18" fill="#2aa3d8"/><rect x="20" y="12" width="8" height="18" fill="#2aa3d8"/></svg></div>
    <div class="benefit-body"><div class="benefit-title">ASSIST PROSECUTION</div><p class="benefit-text">MWTO can assist with the possible prosecution of offenders with records of ...</p></div>
  </div>
  <div class="benefit" style="top:2505px">
    <div class="benefit-icon"><svg width="26" height="30" viewBox="0 0 26 30"><path d="M7 13V9a6 6 0 0 1 12 0v4" fill="none" stroke="#2aa3d8" stroke-width="2.5"/><rect x="3" y="13" width="20" height="15" rx="2" fill="#2aa3d8"/></svg></div>
    <div class="benefit-body"><div class="benefit-title">ACCESS AND SECURITY</div><p class="benefit-text">You can access your data from any PC around the world connected to the Internet.....</p></div>
  </div>
  <a class="btn-more" href="#">READ MORE!</a>
</section>

<section>
  <h2 class="section-title left" style="left:632px;top:1960px;text-align:left">REPORT</h2>
  <p class="report-text" style="top:2042px">Statistical Reports can be done instantaneously and can be run on any data stored with in MWTO. Charts and Graphs are available to clearly show trends and details for Management Purposes.</p>
  <div class="stats">
    <div class="stat"><span class="stat-label">Graffiti type Report (10 -10-2014 to 10-12-2014)</span><span class="stat-bar"><i style="width:50%"></i></span><span class="stat-value">50,5%</span><span class="stat-change"><em>▲</em><br>+20%</span></div>
    <div class="stat"><span class="stat-label">Graffiti type Report (10 -10-2014 to 10-12-2014)</span><span class="stat-bar"><i style="width:20%"></i></span><span class="stat-value">20%</span><span class="stat-change"><em>▼</em><br>-6%</span></div>
    <div class="stat"><span class="stat-label">Graffiti type Report (10 -10-2014 to 10-12-2014)</span><span class="stat-bar"><i style="width:30%"></i></span><span class="stat-value">29.5%</span><span class="stat-change"><em>▲</em><br>+9.7%</span></div>
  </div>
  <svg class="pie" width="240" height="240" viewBox="-120 -120 240 240" role="img" aria-label="Pie chart of graffiti types">
    <path d="M0 0L0 -119A119 119 0 0 1 111.8 40.7Z" fill="#a9a9a9"/>
    <path d="M0 0L111.8 40.7A119 119 0 0 1 -50.3 107.8Z" fill="#3fa0d6"/>
    <path d="M0 0L-50.3 107.8A119 119 0 0 1 -20.7 -117.2Z" fill="#3a3a3a"/>
    <path d="M0 0L-20.7 -117.2A119 119 0 0 1 0 -119Z" fill="#dcdcdc"/>
  </svg>
  <p class="report-text" style="top:2638px">Comparison reports (both historically and geographically) can show the effectiveness of anti graffiti policy. Detail Reports can be run Monthly, Quarterly and Annually.</p>
</section>

<footer class="site-footer">
  <div class="footer-brand">
    <div class="brand-short">MWTO</div>
    <div class="brand-long">MERIDALE WALL TRACKING OFFICE</div>
  </div>
  <p class="copyright">copyright 2014 MWTO all rights reserved</p>
  <div class="footer-contact">
    <h3>CONTACT US</h3>
    <p>Tell Phone: (02) 5550 1234</p>
    <p style="line-height:1.3">enquiries@mwto.example<br>support@mwto.example</p>
  </div>
  <div class="footer-address">Meridale Wall Tracking Office<br>PO Box 418, Meridale, NSW 2990</div>
  <div class="socials"><span></span><span></span><span></span><span></span><span></span></div>
</footer>

</body>
</html>
```